CFO services graphic design

I own a business consulting firm called Marlowe Consulting and we need a graphic for CFO services in our colours and branding. The attached file "CFO services to be put into Marlowe consulting theme", shows the content for the design. The two other files show the theme and colours for the new design.

```html
<!DOCTYPE html>
<html lang="en">
<head>
<meta charset="utf-8">
<title>Marlowe Consulting – Market Leader</title>
<link href="https://fonts.googleapis.com/css2?family=Poppins:wght@400;500;600;700&display=swap" rel="stylesheet">
<style>
  :root{
    --sky:#27aee6;
    --sky-dark:#1d8fcf;
    --navy:#0e2350;
    --deep:#14336f;
    --royal:#1c4fc5;
    --orange:#f2922f;
    --ink:#2f3033;
    --headline:#12285c;
    --rule:#e3e5ea;
    --white:#ffffff;
  }
  html,body{margin:0;padding:0;width:1200px;height:949px;overflow:hidden;background:var(--white);}
  .canvas{display:block;width:1200px;height:949px;}
  .canvas text{font-family:'Poppins',sans-serif;}
  .label{font-size:18px;font-weight:600;fill:var(--ink);letter-spacing:.3px;}
  .hub-title{font-size:23px;font-weight:700;fill:var(--white);}
  .hub-sub{font-size:12px;font-weight:500;fill:var(--white);}
  .core-title{font-size:34px;font-weight:500;fill:var(--white);}
  .brand-name{font-size:34px;font-weight:400;fill:var(--orange);letter-spacing:2px;}
  .tagline{font-size:24px;font-weight:600;fill:var(--headline);}
  .glyph{fill:none;stroke:var(--white);stroke-width:2.2;stroke-linecap:round;stroke-linejoin:round;}
</style>
</head>
<body>
<svg class="canvas" viewBox="128 112 1245 962" preserveAspectRatio="xMidYMid meet" role="img" aria-label="Marlowe Consulting market leader framework">
  <rect x="128" y="112" width="1245" height="962" fill="var(--white)"/>

  <!-- brand -->
  <g class="brand">
    <circle cx="626" cy="230" r="22" fill="var(--orange)"/>
    <text class="brand-name" x="662" y="243">MARLOWE CONSULTING</text>
  </g>

  <!-- connectors -->
  <g class="connectors" stroke-width="4">
    <polyline points="509,329 452,404 419,488" fill="none" stroke="var(--sky)"/>
    <line x1="452" y1="404" x2="567" y2="470" stroke="var(--sky)"/>
    <polyline points="988,330 1041,402 1077,487" fill="none" stroke="var(--navy)"/>
    <line x1="1041" y1="402" x2="930" y2="470" stroke="var(--navy)"/>
    <polyline points="419,668 455,750 512,824" fill="none" stroke="var(--deep)"/>
    <line x1="455" y1="750" x2="564" y2="695" stroke="var(--deep)"/>
    <polyline points="1080,667 1043,752 985,828" fill="none" stroke="var(--royal)"/>
    <line x1="1043" y1="752" x2="928" y2="692" stroke="var(--royal)"/>
  </g>

  <!-- ring -->
  <circle cx="741" cy="597" r="187" fill="none" stroke="var(--sky-dark)" stroke-width="16"/>
  <circle cx="741" cy="597" r="187" fill="none" stroke="var(--sky)" stroke-width="11"/>

  <!-- core -->
  <circle cx="741" cy="597" r="115" fill="var(--white)" stroke="var(--royal)" stroke-width="1.5"/>
  <circle cx="741" cy="597" r="100" fill="var(--orange)"/>
  <text class="core-title" x="741" y="594" text-anchor="middle">MARKET</text>
  <text class="core-title" x="741" y="627" text-anchor="middle">LEADER</text>

  <!-- hubs -->
  <g class="hub">
    <circle cx="567" cy="470" r="70" fill="var(--white)" stroke="var(--sky)" stroke-width="1.5"/>
    <circle cx="567" cy="470" r="61" fill="var(--sky)"/>
    <text class="hub-title" x="567" y="472" text-anchor="middle">GET OUT</text>
    <text class="hub-sub" x="567" y="495" text-anchor="middle">EXIT WITH</text>
    <text class="hub-sub" x="567" y="510" text-anchor="middle">WEALTH</text>
  </g>
  <g class="hub">
    <circle cx="930" cy="470" r="70" fill="var(--white)" stroke="var(--navy)" stroke-width="1.5"/>
    <circle cx="930" cy="470" r="61" fill="var(--navy)"/>
    <text class="hub-title" x="930" y="472" text-anchor="middle">GET FIT</text>
    <text class="hub-sub" x="930" y="495" text-anchor="middle">DISCIPLINE</text>
  </g>
  <g class="hub">
    <circle cx="564" cy="695" r="70" fill="var(--white)" stroke="var(--deep)" stroke-width="1.5"/>
    <circle cx="564" cy="695" r="61" fill="var(--deep)"/>
    <text class="hub-title" x="564" y="676" text-anchor="middle">GET</text>
    <text class="hub-title" x="564" y="700" text-anchor="middle">FUNDED</text>
    <text class="hub-sub" x="564" y="718" text-anchor="middle">ACCESS TO</text>
    <text class="hub-sub" x="564" y="733" text-anchor="middle">CAPITAL</text>
  </g>
  <g class="hub">
    <circle cx="928" cy="692" r="70" fill="var(--white)" stroke="var(--royal)" stroke-width="1.5"/>
    <circle cx="928" cy="692" r="61" fill="var(--royal)"/>
    <text class="hub-title" x="928" y="695" text-anchor="middle">GET BIG</text>
    <text class="hub-sub" x="928" y="715" text-anchor="middle">SCALE</text>
  </g>

  <!-- satellites -->
  <g class="satellites">
    <circle cx="509" cy="329" r="37" fill="var(--sky)"/>
    <circle cx="452" cy="404" r="37" fill="var(--sky)"/>
    <circle cx="419" cy="488" r="37" fill="var(--sky)"/>
    <circle cx="988" cy="330" r="37" fill="var(--navy)"/>
    <circle cx="1041" cy="402" r="37" fill="var(--navy)"/>
    <circle cx="1077" cy="487" r="37" fill="var(--navy)"/>
    <circle cx="419" cy="668" r="37" fill="var(--deep)"/>
    <circle cx="455" cy="750" r="37" fill="var(--deep)"/>
    <circle cx="512" cy="824" r="37" fill="var(--deep)"/>
    <circle cx="1080" cy="667" r="37" fill="var(--royal)"/>
    <circle cx="1043" cy="752" r="37" fill="var(--royal)"/>
    <circle cx="985" cy="828" r="37" fill="var(--royal)"/>
  </g>

  <!-- simple icons -->
  <g class="glyph">
    <path d="M509 312 L525 340 L493 340 Z M509 322 V330 M509 335 V336"/>
    <path d="M440 418 V400 M452 418 V394 M464 418 V404 M436 398 L448 388 L458 394 L468 384"/>
    <path d="M403 496 L413 486 L423 492 L435 480 M405 500 H433"/>
    <path d="M980 344 H996 M983 344 L985 326 H991 L993 344 M983 326 V318 H993 V326"/>
    <path d="M1021 402 Q1041 384 1061 402 Q1041 420 1021 402 Z"/><circle class="glyph" cx="1041" cy="402" r="6"/>
    <circle class="glyph" cx="1077" cy="474" r="5"/><circle class="glyph" cx="1065" cy="498" r="5"/><circle class="glyph" cx="1089" cy="498" r="5"/>
    <path d="M1074 478 L1067 494 M1080 478 L1087 494 M1070 498 H1084"/>
    <path d="M401 652 H437 V680 H401 Z M407 674 L415 664 L423 670 L431 658"/>
    <path d="M455 734 V746 M441 758 V748 H469 V758 M455 748 V758"/><circle class="glyph" cx="455" cy="730" r="4"/>
    <path d="M496 818 L512 810 L528 818 V836 L512 844 L496 836 Z M505 824 L511 830 L520 819"/>
    <circle class="glyph" cx="1080" cy="667" r="9"/><circle class="glyph" cx="1080" cy="667" r="3"/>
    <path d="M1043 742 V762 M1049 745 Q1043 741 1038 745 Q1035 751 1043 752 Q1051 753 1048 759 Q1043 763 1037 759"/>
    <circle class="glyph" cx="977" cy="818" r="5"/><circle class="glyph" cx="993" cy="818" r="5"/>
    <path d="M969 842 Q969 828 977 828 Q985 828 985 842 M985 842 Q985 828 993 828 Q1001 828 1001 842"/>
  </g>

  <!-- labels -->
  <g class="labels">
    <text class="label" x="447" y="293" text-anchor="end">RISK</text>
    <text class="label" x="452" y="315" text-anchor="end">MANAGEMENT</text>
    <text class="label" x="387" y="380" text-anchor="end">PERFORMANCE</text>
    <text class="label" x="387" y="403" text-anchor="end">MONITORING</text>
    <text class="label" x="352" y="493" text-anchor="end">M&amp;A</text>
    <text class="label" x="1051" y="314">STRATEGY</text>
    <text class="label" x="1093" y="392">VISION</text>
    <text class="label" x="1124" y="483">STRUCTURE</text>
    <text class="label" x="355" y="672" text-anchor="end">SYSTEM &amp;</text>
    <text class="label" x="355" y="694" text-anchor="end">PROCESSES</text>
    <text class="label" x="397" y="768" text-anchor="end">SALES &amp;</text>
    <text class="label" x="397" y="790" text-anchor="end">MARKETING</text>
    <text class="label" x="443" y="843" text-anchor="end">PRODUCT &amp;</text>
    <text class="label" x="443" y="865" text-anchor="end">SERVICES</text>
    <text class="label" x="1131" y="680">CULTURE</text>
    <text class="label" x="1103" y="774">FINANCE</text>
    <text class="label" x="1049" y="847">PEOPLE</text>
  </g>

  <!-- footer -->
  <line x1="128" y1="915" x2="1373" y2="915" stroke="var(--rule)" stroke-width="2"/>
  <g class="target" fill="none" stroke="var(--orange)" stroke-width="3">
    <circle cx="430" cy="983" r="40"/>
    <circle cx="430" cy="983" r="30"/>
    <circle cx="430" cy="983" r="19"/>
    <circle cx="430" cy="983" r="8"/>
    <path d="M430 983 L468 945 M458 944 L468 945 L470 955 M463 940 L474 938 L472 949" stroke-linecap="round" stroke-linejoin="round"/>
  </g>
  <text class="tagline" x="500" y="974">Our purpose is clear, we get companies and their</text>
  <text class="tagline" x="500" y="1002">founders, fit, funded, big and out</text>
</svg>
</body>
</html>
```